Personal Injury Lawyer Billboard

I would like a design created featuring the image of the lawyer centered in the middle of the design.
To the left of the lawyer's image it should read "INJURED?"
To the right of the lawyer's image, it should read "CALL BRUNO!"
Under Call Bruno, include the phone number 318-555-0187.
At the bottom of the design include the lawyers information "Bruno Pemberly Accident & Injury Lawyers"
PLEASE REMOVED THE BACKGROUND IMAGERY OF THE PHOTO SUBMITTED. Also, the colors for this design should match the colors shown in the logo (navy, white and relective soft gold). Please use those color combinations in ways that best stand out.

```html
<!DOCTYPE html>
<html lang="en">
<head>
<meta charset="utf-8">
<title>Bruno Pemberly – Accident &amp; Injury Lawyers Billboard</title>
<link rel="stylesheet" href="https://fonts.googleapis.com/css2?family=Noticia+Text:wght@400;700&display=swap">
<style>
  :root {
    --page-bg: #e6e7ea;
    --navy: #1b2244;
    --white: #ffffff;
    --gold: #c9a26a;
    --suit-dark: #1f2a5c;
    --suit-mid: #2c3a78;
    --skin: #b98a6e;
  }
  html, body {
    margin: 0;
    padding: 0;
    width: 1200px;
    height: 999px;
    overflow: hidden;
    background: var(--page-bg);
  }
  .billboard {
    position: absolute;
    left: 40px;
    top: 240px;
    width: 1120px;
    height: 520px;
    background: var(--navy);
    overflow: hidden;
    font-family: "Noticia Text", Georgia, serif;
    color: var(--white);
  }
  .gold-rule {
    position: absolute;
    left: 0;
    width: 100%;
    height: 3px;
    background: var(--gold);
  }
  .gold-rule--top { top: 300px; }
  .gold-rule--bottom { top: 440px; }

  .lawyer-photo {
    position: absolute;
    left: 316px;
    top: 58px;
    width: 366px;
    height: 462px;
    border-radius: 150px 150px 0 0;
    background:
      radial-gradient(ellipse 70px 90px at 50% 80px, var(--skin) 0 98%, transparent 100%),
      linear-gradient(180deg, var(--suit-mid) 0%, var(--suit-dark) 100%);
  }

  .headline {
    position: absolute;
    left: 690px;
    top: 118px;
    width: 400px;
    margin: 0;
    text-align: center;
    font-weight: 700;
    font-size: 82px;
    line-height: 1;
  }

  .call-block {
    position: absolute;
    left: 20px;
    top: 318px;
    width: 290px;
    text-align: center;
  }
  .call-block__prompt {
    margin: 0;
    font-weight: 400;
    font-size: 36px;
    line-height: 1.1;
  }
  .call-block__phone {
    margin: 4px 0 0;
    font-weight: 700;
    font-size: 44px;
    line-height: 1.1;
    letter-spacing: 0.5px;
  }

  .firm-block {
    position: absolute;
    left: 690px;
    top: 322px;
    width: 400px;
    text-align: center;
  }
  .firm-block__name {
    margin: 0;
    font-weight: 700;
    font-size: 44px;
    line-height: 1.1;
  }
  .firm-block__practice {
    margin: 6px 0 0;
    font-weight: 400;
    font-size: 25px;
    line-height: 1.2;
  }
</style>
</head>
<body>
  <section class="billboard">
    <div class="gold-rule gold-rule--top"></div>
    <div class="gold-rule gold-rule--bottom"></div>

    <h1 class="headline">Injured?</h1>

    <div class="call-block">
      <p class="call-block__prompt">Call Bruno!</p>
      <p class="call-block__phone">318-555-0187</p>
    </div>

    <div class="firm-block">
      <p class="firm-block__name">Bruno Pemberly</p>
      <p class="firm-block__practice">Accident &amp; Injury Lawyers</p>
    </div>

    <div class="lawyer-photo" role="img" aria-label="Cut-out portrait of the lawyer in a navy suit, white shirt and green tie, raising a fist"></div>
  </section>
</body>
</html>
```